Business Card Design Project

looking for business cards with new logo

I am looking to keep with the colors of the logo i posted.  Here are some other details to consider.  I would like my website prominently displayed on the business card with the logo.  my website is www.HavenrockTX.com...it should be spelled this way.

My contact information is:

Daniel P Whitcomb III
Broker/Owner
48391 Cordell Ave., Suite 307
Brookmere, Texas 70000
Office: 555-555-0147
Email:  Daniel@HavenrockTX.com

Thank you
Daniel Whitcomb

```html
<!DOCTYPE html>
<html lang="en">
<head>
<meta charset="utf-8">
<title>HavenrockTX Business Cards</title>
<link rel="stylesheet" href="https://fonts.googleapis.com/css2?family=Open+Sans:wght@400;600&display=swap">
<style>
  :root {
    --backdrop: #d9d9db;
    --card: #ffffff;
    --navy: #1d4576;
    --charcoal: #3d3d3f;
    --name-blue: #4d6a8c;
    --text-grey: #5f6469;
    --icon-grey: #6d7276;
    --logo-text: #ffffff;
  }
  * { box-sizing: border-box; margin: 0; padding: 0; }
  html, body { width: 1200px; height: 900px; overflow: hidden; }
  body {
    background: var(--backdrop);
    font-family: "Open Sans", Arial, sans-serif;
    display: flex;
    flex-direction: column;
    align-items: center;
    justify-content: center;
    gap: 40px;
  }
  .business-card {
    position: relative;
    width: 700px;
    height: 400px;
    background: var(--card);
    box-shadow: 0 2px 6px rgba(0,0,0,0.12);
  }
  .logo-panel {
    position: absolute;
    top: 42px;
    right: 42px;
    width: 230px;
    height: 86px;
    display: flex;
    align-items: center;
    justify-content: center;
    gap: 10px;
  }
  .logo-panel--navy { background: var(--navy); }
  .logo-panel--charcoal { background: var(--charcoal); }
  .logo-mark {
    width: 14px; height: 14px;
    background: var(--logo-text);
  }
  .logo-name {
    color: var(--logo-text);
    font-size: 26px;
    font-weight: 400;
    letter-spacing: 0.5px;
  }
  .identity {
    position: absolute;
    left: 42px;
    top: 150px;
    color: var(--name-blue);
  }
  .identity .person-name { font-size: 22px; font-weight: 400; }
  .identity .person-title { font-size: 18px; margin-top: 2px; }
  .contact-list {
    position: absolute;
    left: 42px;
    top: 228px;
    list-style: none;
    color: var(--text-grey);
    font-size: 14px;
    line-height: 1.45;
  }
  .contact-list li {
    display: flex;
    align-items: flex-start;
    gap: 14px;
    margin-bottom: 8px;
  }
  .contact-icon { width: 16px; height: 16px; flex: none; margin-top: 2px; fill: var(--icon-grey); }
</style>
</head>
<body>

<section class="business-card">
  <div class="logo-panel logo-panel--navy">
    <span class="logo-mark"></span>
    <span class="logo-name">HavenrockTX</span>
  </div>
  <div class="identity">
    <p class="person-name">Daniel P Whitcomb III</p>
    <p class="person-title">Broker/Owner</p>
  </div>
  <ul class="contact-list">
    <li>
      <svg class="contact-icon" viewBox="0 0 16 16"><path d="M8 0a5.5 5.5 0 0 0-5.5 5.5C2.5 10 8 16 8 16s5.5-6 5.5-10.5A5.5 5.5 0 0 0 8 0zm0 8a2.5 2.5 0 1 1 0-5 2.5 2.5 0 0 1 0 5z"/></svg>
      <span>48391 Cordell Ave., Suite 307<br>Brookmere, Texas 70000</span>
    </li>
    <li>
      <svg class="contact-icon" viewBox="0 0 16 16"><path d="M3.6 1l2.3 3-1.4 1.8a9 9 0 0 0 5.7 5.7L12 10.1l3 2.3-1.3 2.6C7 15 1 9 1 2.3z"/></svg>
      <span>555-555-0147</span>
    </li>
    <li>
      <svg class="contact-icon" viewBox="0 0 16 16"><path d="M1 3h14v10H1zm1.5 1.4v.3L8 8.6l5.5-3.9v-.3z"/></svg>
      <span>Daniel@HavenrockTX.com</span>
    </li>
    <li>
      <svg class="contact-icon" viewBox="0 0 16 16"><path d="M8 0a8 8 0 1 0 0 16A8 8 0 0 0 8 0zm0 1.5c.8 0 1.9 1.8 2.2 5.5H5.8C6.1 3.3 7.2 1.5 8 1.5zM1.6 9h2.7c.1 2 .5 3.6 1.1 4.7A6.5 6.5 0 0 1 1.6 9zm0-2A6.5 6.5 0 0 1 5.4 2.3C4.8 3.4 4.4 5 4.3 7zm4.2 2h4.4C9.9 12.7 8.8 14.5 8 14.5S6.1 12.7 5.8 9zm4.8 4.7c.6-1.1 1-2.7 1.1-4.7h2.7a6.5 6.5 0 0 1-3.8 4.7zM11.7 7c-.1-2-.5-3.6-1.1-4.7A6.5 6.5 0 0 1 14.4 7z"/></svg>
      <span>www.HavenrockTX.com</span>
    </li>
  </ul>
</section>

<section class="business-card">
  <div class="logo-panel logo-panel--charcoal">
    <span class="logo-mark"></span>
    <span class="logo-name">HavenrockTX</span>
  </div>
  <div class="identity">
    <p class="person-name">Daniel P Whitcomb III</p>
    <p class="person-title">Broker/Owner</p>
  </div>
  <ul class="contact-list">
    <li>
      <svg class="contact-icon" viewBox="0 0 16 16"><path d="M8 0a5.5 5.5 0 0 0-5.5 5.5C2.5 10 8 16 8 16s5.5-6 5.5-10.5A5.5 5.5 0 0 0 8 0zm0 8a2.5 2.5 0 1 1 0-5 2.5 2.5 0 0 1 0 5z"/></svg>
      <span>48391 Cordell Ave., Suite 307<br>Brookmere, Texas 70000</span>
    </li>
    <li>
      <svg class="contact-icon" viewBox="0 0 16 16"><path d="M3.6 1l2.3 3-1.4 1.8a9 9 0 0 0 5.7 5.7L12 10.1l3 2.3-1.3 2.6C7 15 1 9 1 2.3z"/></svg>
      <span>555-555-0147</span>
    </li>
    <li>
      <svg class="contact-icon" viewBox="0 0 16 16"><path d="M1 3h14v10H1zm1.5 1.4v.3L8 8.6l5.5-3.9v-.3z"/></svg>
      <span>Daniel@HavenrockTX.com</span>
    </li>
    <li>
      <svg class="contact-icon" viewBox="0 0 16 16"><path d="M8 0a8 8 0 1 0 0 16A8 8 0 0 0 8 0zm0 1.5c.8 0 1.9 1.8 2.2 5.5H5.8C6.1 3.3 7.2 1.5 8 1.5zM1.6 9h2.7c.1 2 .5 3.6 1.1 4.7A6.5 6.5 0 0 1 1.6 9zm0-2A6.5 6.5 0 0 1 5.4 2.3C4.8 3.4 4.4 5 4.3 7zm4.2 2h4.4C9.9 12.7 8.8 14.5 8 14.5S6.1 12.7 5.8 9zm4.8 4.7c.6-1.1 1-2.7 1.1-4.7h2.7a6.5 6.5 0 0 1-3.8 4.7zM11.7 7c-.1-2-.5-3.6-1.1-4.7A6.5 6.5 0 0 1 14.4 7z"/></svg>
      <span>www.HavenrockTX.com</span>
    </li>
  </ul>
</section>

</body>
</html>
```